RW SURFACING CONTRACTORS LTD PRESENTATION FOLDER

I need a Presentation Folder please to contain information about our services.

We are a Flooring Contractor - for information about our business please view our website: www.rwsurfacing.co.nz

Please refer to our new brochure attached - it must fit this style and suit our brand.
Look forward to your ideas.

Also our logo needs a couple of quick changes -
Refer attached - can you please change a line and add a line -

logo
Concrete Grinding and Polishing
Resin Floors and Floor Toppings
Concrete Prep and Non Slip Coatings

Thanks Tess
Updates

Hi ALL - I just need a simple PRESENTATION FOLDER.

I already have a brochure so I don't need the same information again on my Presentation Folder.
Just something simple - with just our logo really - for ideas look at Presentation folders at Orbel Press.
I just like the colours and style of the brochure and thought these could help you.
The presentation folder will house that brochure and other bits of information.
I hope this helps
TessĀ 

I just added our revised logo - and gave more specific details about what we are after - refer notes.

Thanks, TessĀ 

Industry/Entity Type

Business

Requirements
Must have
• I just added our updated LOGO - thought this would help match the blue.

I would like LOGO on front page with key words Quality, Value, Experience.
Plain blue inside
Back please add our guarantee, and contact details including website and email etc.

This one will come down to lay out which must match our brochure which was provided. Thank you.

```html
<!DOCTYPE html>
<html lang="en">
<head>
<meta charset="utf-8">
<title>RW Surfacing Contractors – Presentation Folder</title>
<link href="https://fonts.googleapis.com/css2?family=Quicksand:wght@500;600;700&family=Arimo:wght@400;700&display=swap" rel="stylesheet">
<style>
  :root {
    --blue: #3f7bc4;
    --blue-deep: #2f66b0;
    --blue-soft: #5b93d3;
    --red: #e33b2a;
    --paper: #ececec;
    --white: #ffffff;
    --ink: #1a1a1a;
    --ink-soft: #555555;
    --stage: #f0f0f0;
  }
  * { box-sizing: border-box; margin: 0; padding: 0; }
  html, body { width: 960px; height: 1200px; overflow: hidden; }
  body { background: var(--stage); font-family: "Quicksand", sans-serif; position: relative; }

  .spread { position: absolute; display: flex; }
  .spread--outside { left: 180px; top: 50px; width: 600px; height: 590px; box-shadow: 0 14px 30px rgba(0,0,0,.12); }
  .spread--inside { left: 218px; top: 670px; width: 524px; height: 488px; }

  .panel { position: relative; width: 300px; height: 590px; overflow: hidden; }
  .panel__art { position: absolute; inset: 0; }

  /* back cover */
  .contact-tab { position: absolute; left: 0; top: 36px; width: 112px; height: 22px; background: var(--blue); border-right: 6px solid var(--red); color: var(--white); font-size: 10.5px; font-weight: 600; line-height: 22px; padding-left: 9px; }
  .contact { position: absolute; left: 10px; top: 110px; width: 140px; color: var(--ink-soft); font-size: 7px; font-weight: 500; }
  .contact__name { color: var(--blue); font-size: 9.5px; font-weight: 600; white-space: nowrap; }
  .contact__address { margin: 2px 0 14px; color: var(--ink); }
  .contact__row { display: flex; margin-bottom: 6px; white-space: nowrap; }
  .contact__label { width: 54px; }
  .contact__value { color: var(--ink); }
  .region-map { position: absolute; left: 150px; top: 32px; width: 144px; height: 190px; border-radius: 6px; background: linear-gradient(160deg, #6d9fd8, var(--blue-deep)); }
  .guarantee-mark { position: absolute; left: 88px; top: 236px; width: 124px; height: 150px; border-radius: 8px; background: radial-gradient(circle at 50% 45%, #ea4a36 0%, #d93222 60%, #c42d20 100%); }
  .guarantee { position: absolute; left: 0; right: 0; top: 410px; text-align: center; color: var(--white); padding: 0 6px; }
  .guarantee__title { font-size: 15px; font-weight: 700; margin-bottom: 16px; }
  .guarantee__lead { font-size: 10px; font-weight: 600; line-height: 1.6; margin-bottom: 14px; white-space: nowrap; }
  .guarantee__note { font-size: 7.5px; font-weight: 600; line-height: 1.6; white-space: nowrap; }

  /* front cover */
  .brand { position: absolute; left: 0; right: 0; top: 210px; text-align: center; }
  .brand__mark { display: inline-flex; align-items: center; gap: 8px; }
  .brand__square { width: 20px; height: 20px; background: var(--red); }
  .brand__name { font-family: "Arimo", sans-serif; font-weight: 700; font-size: 19px; color: var(--ink); line-height: 1.05; text-align: left; }
  .brand__services { margin-top: 12px; font-family: "Arimo", sans-serif; font-size: 10px; line-height: 1.35; color: var(--ink); }
  .keywords { position: absolute; right: 16px; top: 470px; text-align: right; color: var(--white); font-size: 30px; font-weight: 700; line-height: 1.4; }

  /* inside */
  .inside-art { position: absolute; inset: 0; }
  .business-card { position: absolute; left: 62px; top: 378px; width: 122px; height: 56px; background: var(--white); box-shadow: 0 3px 6px rgba(0,0,0,.2); font-size: 7.5px; font-weight: 700; color: var(--ink); display: flex; align-items: center; justify-content: center; }
  .inside-phone { position: absolute; left: 64px; top: 452px; color: var(--white); font-size: 14px; font-weight: 700; display: flex; align-items: center; gap: 5px; }
  .insert { position: absolute; left: 350px; top: 112px; width: 126px; height: 330px; background: var(--white); box-shadow: 0 4px 10px rgba(0,0,0,.25); overflow: hidden; }
  .insert__photo { height: 236px; background: linear-gradient(180deg, #cfd8e2 0%, #8fb6d6 45%, #3b5f7a 100%); }
  .insert__brand { text-align: center; padding-top: 12px; }
  .insert__name { display: inline-flex; align-items: center; gap: 4px; font-family: "Arimo", sans-serif; font-weight: 700; font-size: 9px; color: var(--ink); }
  .insert__square { width: 8px; height: 8px; background: var(--red); }
  .insert__services { font-family: "Arimo", sans-serif; font-size: 4px; line-height: 1.4; color: var(--ink); margin-top: 3px; }
  .insert__keyword { position: absolute; left: 10px; bottom: 8px; color: var(--blue); font-weight: 700; font-size: 13px; }
</style>
</head>
<body>

<section class="spread spread--outside" aria-label="Folder outside">
  <article class="panel panel--back">
    <svg class="panel__art" viewBox="0 0 300 590" preserveAspectRatio="none">
      <defs>
        <radialGradient id="backGlow" cx="0.5" cy="0.15" r="0.6">
          <stop offset="0" stop-color="#6cc3e0"/>
          <stop offset="0.5" stop-color="#3f7bc4"/>
          <stop offset="1" stop-color="#3a74bd"/>
        </radialGradient>
      </defs>
      <rect width="300" height="590" fill="var(--paper)"/>
      <path d="M0 268 Q150 340 300 252 V590 H0 Z" fill="url(#backGlow)"/>
    </svg>
    <div class="contact-tab">Contact Details</div>
    <div class="region-map" role="img" aria-label="Map of New Zealand with a pin and label marking Auckland"></div>
    <div class="contact">
      <p class="contact__name">RW SURFACING CONTRACTORS</p>
      <p class="contact__address">PO Box 412, Auckland 0600</p>
      <p class="contact__row"><span class="contact__label">Free Phone:</span><span class="contact__value">0800 555 017</span></p>
      <p class="contact__row"><span class="contact__label">Email:</span><span class="contact__value">info@rwsurfacing.co.nz</span></p>
      <p class="contact__row"><span class="contact__label">Fax:</span><span class="contact__value">09 555 0182</span></p>
      <p class="contact__row"><span class="contact__label">Website:</span><span class="contact__value">www.rwsurfacing.co.nz</span></p>
    </div>
    <div class="guarantee-mark" role="img" aria-label="Large red star emblem for the guarantee"></div>
    <div class="guarantee">
      <h2 class="guarantee__title">Our guarantee to you :</h2>
      <p class="guarantee__lead">Have complete peace of mind when dealing with us,<br>as we provide a workmanship guarantee on all services.</p>
      <p class="guarantee__note">Arrange your free quote and consultation for concrete polishing, concrete<br>preparation, non-slip coatings or resin floor toppings</p>
    </div>
  </article>

  <article class="panel panel--front">
    <svg class="panel__art" viewBox="0 0 300 590" preserveAspectRatio="none">
      <defs>
        <linearGradient id="frontRed" x1="0" y1="0" x2="1" y2="0">
          <stop offset="0" stop-color="#d93222"/>
          <stop offset="1" stop-color="#ea4a36"/>
        </linearGradient>
      </defs>
      <rect width="300" height="590" fill="var(--blue)"/>
      <rect width="300" height="200" fill="url(#frontRed)"/>
      <path d="M0 180 Q110 70 300 112 V370 Q190 470 0 462 Z" fill="var(--blue-deep)"/>
      <path d="M0 192 Q110 84 300 120 V350 Q190 452 0 450 Z" fill="#f1f1f1"/>
      <path d="M0 450 Q190 452 300 350 V372 Q200 470 0 462 Z" fill="var(--red)"/>
    </svg>
    <div class="brand">
      <div class="brand__mark">
        <span class="brand__square"></span>
        <span class="brand__name">RW SURFACING<br>CONTRACTORS</span>
      </div>
      <p class="brand__services">Concrete Grinding &amp; Polishing<br>Resin Floors and Floor Toppings<br>Concrete Prep and Non Slip Coatings</p>
    </div>
    <p class="keywords">Experience,<br>Quality, Value</p>
  </article>
</section>

<section class="spread spread--inside" aria-label="Folder inside">
  <svg class="inside-art" viewBox="0 0 524 488" preserveAspectRatio="none">
    <defs>
      <linearGradient id="insideBlue" x1="0" y1="0" x2="1" y2="1">
        <stop offset="0" stop-color="var(--blue-soft)"/>
        <stop offset="0.5" stop-color="var(--blue)"/>
        <stop offset="1" stop-color="var(--blue-soft)"/>
      </linearGradient>
    </defs>
    <path d="M0 0 H238 Q262 42 286 0 H524 V488 H0 Z" fill="url(#insideBlue)"/>
    <path d="M160 370 Q300 300 524 352 V380 H160 Z" fill="var(--red)"/>
    <path d="M180 380 Q300 320 524 362 V392 H180 Z" fill="#f1f1f1"/>
    <path d="M0 366 H230 L262 455 L294 366 H524 V488 H0 Z" fill="var(--blue)"/>
    <path d="M0 366 H230 L262 455 L294 366 H524" fill="none" stroke="rgba(255,255,255,.25)" stroke-width="1"/>
  </svg>
  <div class="business-card">Business Card</div>
  <div class="inside-phone">
    <svg width="11" height="11" viewBox="0 0 24 24" aria-hidden="true"><path fill="#fff" d="M6.6 10.8a15 15 0 0 0 6.6 6.6l2.2-2.2c.3-.3.7-.4 1-.2 1.1.4 2.3.6 3.6.6.6 0 1 .4 1 1V20c0 .6-.4 1-1 1C10.6 21 3 13.4 3 4c0-.6.4-1 1-1h3.5c.6 0 1 .4 1 1 0 1.3.2 2.5.6 3.6.1.3 0 .7-.2 1z"/></svg>
    0800-555-017
  </div>
  <div class="insert">
    <div class="insert__photo" role="img" aria-label="Brochure cover photos of a modern house with polished concrete pool surrounds and floors"></div>
    <div class="insert__brand">
      <span class="insert__name"><span class="insert__square"></span>RW SURFACING</span>
      <p class="insert__services">Grinding &amp; Polishing<br>Resin Floors<br>Non Slip Coatings</p>
    </div>
    <p class="insert__keyword">Experience,</p>
  </div>
</section>

</body>
</html>
```